Harbor Light Wellness and Advising, LLC

We need a business card and stationary designed for a new therapy practice for Marcia Tolland. Marcia Tolland is a Therapist who specializes in Therapy for children dealing with trauma and/or stress. Below are some of her thoughts:
colors can include purple, blue, turquoise and green (does NOT have to be all colors) See attached Logos
Marcia Tolland, LMHC
Harbor Light Wellness & Wellness Inc.
4823 W. Quarry Boulevard
Suite 517
Boca Raton, FL 33412
Phone: 561-730-2254
Fax: 561-730-2255
Email: marcia@harborlightwa.example
Website: www.harborlightwa.example

```html
<!DOCTYPE html>
<html lang="en">
<head>
<meta charset="utf-8">
<title>Harbor Light Wellness and Advising – Business Card</title>
<link rel="stylesheet" href="https://fonts.googleapis.com/css2?family=Source+Sans+3:wght@300;400;600&display=swap">
<style>
  :root {
    --green: #87a03a;
    --grey: #6d6e71;
    --text: #656565;
    --card: #ffffff;
    --edge: #dcdcdc;
    --page: #ffffff;
  }
  * { margin: 0; padding: 0; box-sizing: border-box; }
  html, body {
    width: 1200px; height: 1000px; overflow: hidden;
    background: var(--page);
    font-family: "Source Sans 3", "Myriad Pro", sans-serif;
  }
  .card {
    position: absolute; left: 100px; top: 183px;
    width: 1000px; height: 634px;
    background: var(--card);
    border: 1px solid var(--edge);
  }
  .brand {
    position: absolute; left: 56px; top: 88px;
    width: 380px;
    display: flex; align-items: center; gap: 18px;
  }
  .brand-dot {
    flex: none; width: 64px; height: 64px; border-radius: 50%;
    background: var(--grey);
  }
  .brand-name {
    color: var(--green); font-weight: 600;
    font-size: 38px; line-height: 1.08; letter-spacing: 0.5px;
  }
  .holder {
    position: absolute; right: 57px; top: 106px; text-align: right;
  }
  .holder-name {
    color: var(--green); font-weight: 600; font-size: 47px; line-height: 1;
  }
  .holder-title {
    color: var(--text); font-weight: 400; font-size: 37px; line-height: 1; margin-top: 14px;
  }
  .contact {
    position: absolute; right: 57px; top: 341px;
    list-style: none; text-align: right;
  }
  .contact li {
    display: flex; justify-content: flex-end; align-items: center; gap: 10px;
    color: var(--text); font-weight: 300; font-size: 29px;
    height: 58.5px;
  }
  .address {
    position: absolute; left: 56px; top: 436px;
    display: flex; gap: 10px;
    color: var(--text); font-weight: 300; font-size: 29px; line-height: 40px;
    font-style: normal;
  }
  .tag { flex: none; width: 30px; height: 32px; display: block; }
  .address .tag { margin-top: 4px; }
  .tag text { font-family: "Source Sans 3", sans-serif; font-weight: 600; font-size: 17px; fill: var(--grey); }
  .tag .bracket { fill: none; stroke: var(--green); stroke-width: 3.5; }
</style>
</head>
<body>
  <div class="card">
    <div class="brand">
      <span class="brand-dot"></span>
      <span class="brand-name">Harbor Light Wellness and Advising, Inc.</span>
    </div>

    <div class="holder">
      <div class="holder-name">Marcia Tolland</div>
      <div class="holder-title">LMHC</div>
    </div>

    <address class="address">
      <svg class="tag" viewBox="0 0 30 32" aria-hidden="true">
        <path class="bracket" d="M8 2H3V30H8M22 2H27V30H22"/>
        <path d="M15 7c-3.3 0-5.5 2.4-5.5 5.3 0 3.8 5.5 10.2 5.5 10.2s5.5-6.4 5.5-10.2C20.5 9.4 18.3 7 15 7z" fill="var(--grey)"/>
        <circle cx="15" cy="12.4" r="2" fill="#fff"/>
      </svg>
      <span>4823 W. Quarry Boulevard<br>Suite 517<br>Boca Raton, FL 33412</span>
    </address>

    <ul class="contact">
      <li><span>561-730-2254</span>
        <svg class="tag" viewBox="0 0 30 32" aria-label="Phone"><path class="bracket" d="M8 2H3V30H8M22 2H27V30H22"/><text x="15" y="22" text-anchor="middle">T</text></svg></li>
      <li><span>561-730-2255</span>
        <svg class="tag" viewBox="0 0 30 32" aria-label="Fax"><path class="bracket" d="M8 2H3V30H8M22 2H27V30H22"/><text x="15" y="22" text-anchor="middle">F</text></svg></li>
      <li><span>marcia@harborlightwa.example</span>
        <svg class="tag" viewBox="0 0 30 32" aria-label="Email"><path class="bracket" d="M8 2H3V30H8M22 2H27V30H22"/><text x="15" y="22" text-anchor="middle">@</text></svg></li>
      <li><span>www.harborlightwa.example</span>
        <svg class="tag" viewBox="0 0 30 32" aria-label="Website"><path class="bracket" d="M8 2H3V30H8M22 2H27V30H22"/><text x="15" y="22" text-anchor="middle">W</text></svg></li>
    </ul>
  </div>
</body>
</html>
```